Amber Lantern Cafe Business Card

We need a business card design for a new European Cafe. Main menu will be coffee and deserts.

Requirements
Must have
• Logo - 1 of the attached versions
Address - TBA (you can use 487 Morrow Ave Unit 9 for now)
Phone - TBA (you can use 555-238-4176 for now)

```html
<!DOCTYPE html>
<html lang="en">
<head>
<meta charset="utf-8">
<title>Amber Lantern Cafe – Business Card</title>
<link rel="stylesheet" href="https://fonts.googleapis.com/css2?family=Oswald:wght@400;500&display=swap">
<style>
  :root {
    --page: #e8e5df;
    --card: #5e5446;
    --cream: #d9cba4;
    --font: "Oswald", "Arial Narrow", sans-serif;
  }
  * { box-sizing: border-box; margin: 0; padding: 0; }
  html, body { width: 1200px; height: 1200px; overflow: hidden; }
  body {
    background: var(--page);
    font-family: var(--font);
    color: var(--cream);
    position: relative;
  }
  .sprites { position: absolute; width: 0; height: 0; }
  .card {
    position: absolute;
    left: 120px;
    width: 960px;
    height: 540px;
  }
  .card--front { top: 40px; }
  .card--back { top: 620px; }
  .card__shape { position: absolute; inset: 0; width: 960px; height: 540px; }
  .card__body {
    fill: var(--card);
  }
  .card__frame {
    fill: none;
    stroke: var(--cream);
    stroke-width: 2;
  }
  .star { fill: var(--cream); }

  .front__content {
    position: absolute;
    inset: 0;
    display: flex;
    flex-direction: column;
    align-items: center;
    text-align: center;
  }
  .holder {
    margin-top: 68px;
    display: flex;
    align-items: center;
    gap: 14px;
  }
  .holder__stars { display: flex; align-items: center; gap: 10px; }
  .holder__stars svg { fill: var(--cream); }
  .holder__name {
    font-size: 46px;
    font-weight: 500;
    letter-spacing: 1px;
    line-height: 1;
    padding: 0 6px;
  }
  .holder__role {
    font-size: 13px;
    letter-spacing: 1px;
    margin-top: 6px;
  }
  .brand {
    display: flex;
    align-items: center;
    gap: 14px;
    margin-top: 46px;
  }
  .brand__mark {
    width: 58px;
    height: 58px;
    background: var(--cream);
  }
  .brand__name {
    font-size: 34px;
    font-weight: 400;
    letter-spacing: 0.5px;
  }
  .contact {
    margin-top: 62px;
    font-size: 24px;
    font-weight: 400;
    letter-spacing: 0.5px;
    display: flex;
    flex-direction: column;
    align-items: center;
    gap: 26px;
  }
  .contact__line { text-decoration: underline; text-underline-offset: 5px; }

  .back__content {
    position: absolute;
    inset: 0;
    display: flex;
    flex-direction: column;
    align-items: center;
  }
  .back__mark {
    margin-top: 130px;
    width: 120px;
    height: 120px;
    background: var(--cream);
  }
  .back__name {
    margin-top: 22px;
    font-size: 46px;
    font-weight: 400;
    letter-spacing: 0.5px;
    line-height: 1;
  }
</style>
</head>
<body>
  <svg class="sprites" aria-hidden="true">
    <defs>
      <symbol id="star" viewBox="0 0 24 24">
        <polygon points="12,1 15,9 23,9 16.5,14 19,22.5 12,17.5 5,22.5 7.5,14 1,9 9,9"/>
      </symbol>
    </defs>
  </svg>

  <section class="card card--front" aria-label="Business card front">
    <svg class="card__shape" viewBox="0 0 960 540" aria-hidden="true">
      <path class="card__body" d="M44,0 H916 A44 44 0 0 0 960 44 V496 A44 44 0 0 0 916 540 H44 A44 44 0 0 0 0 496 V44 A44 44 0 0 0 44 0 Z"/>
      <path class="card__frame" d="M80,18 H880 A62 62 0 0 0 942 80 V460 A62 62 0 0 0 880 522 H80 A62 62 0 0 0 18 460 V80 A62 62 0 0 0 80 18 Z"/>
      <path class="card__frame" d="M100,28 H860 A72 72 0 0 0 932 100 V440 A72 72 0 0 0 860 512 H100 A72 72 0 0 0 28 440 V100 A72 72 0 0 0 100 28 Z"/>
    </svg>
    <div class="front__content">
      <div class="holder">
        <div class="holder__stars" aria-hidden="true">
          <svg width="20" height="20"><use href="#star"/></svg>
          <svg width="24" height="24"><use href="#star"/></svg>
          <svg width="36" height="36"><use href="#star"/></svg>
        </div>
        <h1 class="holder__name">MARCUS HALE</h1>
        <div class="holder__stars" aria-hidden="true">
          <svg width="36" height="36"><use href="#star"/></svg>
          <svg width="24" height="24"><use href="#star"/></svg>
          <svg width="20" height="20"><use href="#star"/></svg>
        </div>
      </div>
      <p class="holder__role">MANAGER</p>
      <div class="brand">
        <span class="brand__mark" aria-hidden="true"></span>
        <span class="brand__name">Amber Lantern Cafe</span>
      </div>
      <div class="contact">
        <p>CONTACT:</p>
        <p class="contact__line">P: 555-238-4176</p>
        <p class="contact__line">A: 487 MORROW AVE UNIT 9</p>
      </div>
    </div>
  </section>

  <section class="card card--back" aria-label="Business card back">
    <svg class="card__shape" viewBox="0 0 960 540" aria-hidden="true">
      <path class="card__body" d="M44,0 H916 A44 44 0 0 0 960 44 V496 A44 44 0 0 0 916 540 H44 A44 44 0 0 0 0 496 V44 A44 44 0 0 0 44 0 Z"/>
      <path class="card__frame" d="M80,18 H880 A62 62 0 0 0 942 80 V460 A62 62 0 0 0 880 522 H80 A62 62 0 0 0 18 460 V80 A62 62 0 0 0 80 18 Z"/>
      <path class="card__frame" d="M100,28 H860 A72 72 0 0 0 932 100 V440 A72 72 0 0 0 860 512 H100 A72 72 0 0 0 28 440 V100 A72 72 0 0 0 100 28 Z"/>
      <g class="star">
        <use href="#star" x="238" y="166" width="30" height="30"/>
        <use href="#star" x="320" y="80" width="34" height="34"/>
        <use href="#star" x="422" y="48" width="30" height="30"/>
        <use href="#star" x="526" y="48" width="40" height="40"/>
        <use href="#star" x="624" y="92" width="34" height="34"/>
        <use href="#star" x="702" y="185" width="28" height="28"/>
        <use href="#star" x="238" y="345" width="28" height="28"/>
        <use href="#star" x="320" y="424" width="34" height="34"/>
        <use href="#star" x="420" y="458" width="38" height="38"/>
        <use href="#star" x="528" y="456" width="34" height="34"/>
        <use href="#star" x="626" y="416" width="30" height="30"/>
        <use href="#star" x="700" y="328" width="28" height="28"/>
      </g>
    </svg>
    <div class="back__content">
      <span class="back__mark" aria-hidden="true"></span>
      <p class="back__name">Amber Lantern Cafe</p>
    </div>
  </section>
</body>
</html>
```